innovative investment real estate sales firm

We are a uniquely collabrative firm that seeks to bring a conultative approach to uncovering hidden opportunities for our clients, our website needs to convey our client focused approach. Our firm specializes in the sale of apartment properties in Southern California. We have a team of researchers, transaction coordinators and marketing personal to support our geographically specialized advisers. We need a website that introduces clients to our unique way of better helping them achieve their investment goals.

Target Market(s)

High net worth individuals and families

Industry/Entity Type

Real Estate Agent

Font styles to use
Other font styles liked:
• please use font provided

Requirements
Must have
• Stories of our recent projects
• Features on our people
• email capture for viewing inventory
• content that showcases our unique consultative approach that uncovers unrealized opportunities

```html
<!DOCTYPE html>
<html lang="en">
<head>
<meta charset="utf-8">
<title>Meridian Advisers</title>
<link href="https://fonts.googleapis.com/css2?family=Lato:wght@400;700;900&family=Montserrat:wght@400;500;600&display=swap" rel="stylesheet">
<style>
:root{
  --teal:#10a4c0;
  --teal-dark:#0b8ea7;
  --lime:#8dc63f;
  --ink:#2b2f33;
  --body:#3a3a3a;
  --muted:#6d6d6d;
  --topbar:#404b55;
  --footer:#434e58;
  --bottom:#2e2f31;
  --grey-bg:#efefef;
  --line:#dcdcdc;
  --white:#ffffff;
}
*{box-sizing:border-box;margin:0;padding:0}
html,body{width:1200px;height:2490px;overflow:hidden;background:var(--white)}
body{font-family:"Lato",Arial,sans-serif;color:var(--body);position:relative}
.page{position:relative;width:1200px;height:2490px;overflow:hidden}
a{color:inherit;text-decoration:none}

/* top bar */
.topbar{position:absolute;left:0;top:0;width:1200px;height:47px;background:var(--topbar);color:var(--white);font-size:14px}
.topbar .contact{position:absolute;left:80px;top:0;height:47px;display:flex;align-items:center;gap:26px}
.topbar .contact span{display:flex;align-items:center;gap:10px;font-weight:700}
.topbar .contact span.mail{font-weight:400;font-size:13px}
.ring{width:28px;height:28px;border:2px solid var(--white);border-radius:50%;display:flex;align-items:center;justify-content:center}
.social{display:flex;gap:6px}
.topbar .social{position:absolute;right:85px;top:8px}
.social i{display:block;width:31px;height:31px;border-radius:50%;background:var(--teal);border:2px solid var(--white)}

/* header */
.header{position:absolute;left:0;top:47px;width:1200px;height:106px;background:var(--white)}
.brand{position:absolute;left:80px;top:33px;display:flex;align-items:center;gap:12px}
.brand .mark{width:40px;height:40px;background:var(--teal)}
.brand .name{font-family:"Montserrat",Arial,sans-serif;font-weight:600;font-size:20px;color:var(--topbar);letter-spacing:1px;line-height:1}
.nav{position:absolute;right:80px;top:0;height:106px;display:flex;align-items:center;gap:34px;font-family:"Montserrat",Arial,sans-serif;font-weight:500;font-size:13.5px;color:var(--ink)}
.nav a{display:flex;align-items:center;gap:7px}
.caret{width:0;height:0;border-left:4px solid transparent;border-right:4px solid transparent;border-top:5px solid var(--ink)}

/* hero */
.hero{position:absolute;left:0;top:153px;width:1200px;height:511px;background:linear-gradient(180deg,#2f4a6e 0%,#6f9fcf 35%,#c8dcef 55%,#5d82ad 80%,#2b3d58 100%)}
.hero h1{position:absolute;left:0;right:0;top:216px;text-align:center;font-family:"Montserrat",Arial,sans-serif;font-weight:600;font-size:25px;line-height:37px;color:#111;text-shadow:0 0 12px rgba(255,255,255,.7)}
.dots{display:flex;gap:6px;justify-content:center}
.hero .dots{position:absolute;left:0;right:0;bottom:20px}
.dots i{width:12px;height:12px;border-radius:50%;background:var(--white);display:block}
.hero .dots i:first-child{background:var(--teal);border:2px solid var(--white)}

/* section titles */
.title{font-family:"Montserrat",Arial,sans-serif;font-size:29px;font-weight:500;color:var(--topbar);text-align:center;display:flex;align-items:center;justify-content:center;gap:16px;letter-spacing:.5px}
.title::before,.title::after{content:"";width:38px;height:2px;background:var(--topbar)}
.title em{font-style:normal;color:var(--teal)}

/* welcome */
.welcome{position:absolute;left:0;top:664px;width:1200px;height:337px;background:var(--white)}
.welcome .title{position:absolute;left:0;right:0;top:43px}
.welcome .lead{position:absolute;left:0;right:0;top:108px;text-align:center;font-weight:700;font-size:18px;color:#111}
.welcome .copy{position:absolute;left:92px;right:92px;top:146px;text-align:center;font-size:15px;line-height:27px;color:var(--body)}
.btn{display:inline-block;background:var(--teal);color:var(--white);font-weight:700;font-size:15px;padding:0 14px;height:40px;line-height:40px}
.welcome .btn{position:absolute;left:542px;top:254px}

/* featured */
.featured{position:absolute;left:0;top:1001px;width:1200px;height:681px;background:var(--grey-bg)}
.featured .title{position:absolute;left:0;right:0;top:38px}
.card{position:absolute;top:111px;width:328px;height:474px;background:var(--white);border:1px solid var(--line)}
.card .photo{height:206px;position:relative}
.card .tag{position:absolute;left:0;top:0;width:80px;height:38px;background:var(--lime);color:var(--white);font-weight:700;font-size:15px;display:flex;align-items:center;justify-content:center}
.card .bar{height:46px;background:var(--teal);display:flex;align-items:center;justify-content:space-between;padding:0 20px;color:var(--white);font-weight:700;font-size:14px}
.card .bar span{display:flex;align-items:center;gap:10px}
.card .price{background:#3f4a54;height:28px;line-height:28px;padding:0 12px;font-weight:400;font-size:14px}
.card h3{font-size:17px;font-weight:700;color:#111;margin:24px 20px 10px}
.card p{font-size:13px;line-height:20px;color:var(--body);margin:0 20px}
.card .meta{position:absolute;left:0;right:0;bottom:0;height:60px;border-top:1px solid var(--line);display:flex;align-items:center;gap:26px;padding:0 20px;font-size:12.5px;color:var(--muted)}
.card .meta span{display:flex;align-items:center;gap:7px}
.featured .dots{position:absolute;left:0;right:0;top:624px}
.featured .dots i{width:10px;height:10px;background:#d3d3d3}
.featured .dots i:first-child{background:var(--teal)}

/* team */
.team{position:absolute;left:0;top:1682px;width:1200px;height:459px;background:var(--white)}
.team .title{position:absolute;left:0;right:0;top:44px}
.member{position:absolute;top:111px;width:240px}
.member .photo{height:242px}
.member .name{height:43px;line-height:43px;text-align:center;font-size:13.5px;font-weight:700;color:var(--ink);border-bottom:3px solid #cfcfcf}
.member.active .name{border-bottom-color:var(--lime);display:flex;align-items:center;justify-content:center;gap:20px}
.member.active .name i{width:11px;height:11px;border-radius:50%;background:#5a5a5a;display:block}
.member .overlay{position:absolute;left:0;right:0;top:180px;text-align:center;color:var(--white);font-size:13px;font-weight:700;line-height:20px}
.member .overlay small{display:block;font-weight:400;font-size:12px}

/* footer */
.footer{position:absolute;left:0;top:2141px;width:1200px;height:299px;background:var(--footer);color:var(--white)}
.inquiry{position:absolute;left:91px;top:-11px;width:294px;height:277px;background:var(--teal);padding:20px 22px}
.inquiry h4{font-size:18px;font-weight:700;margin-bottom:20px;letter-spacing:.3px}
.inquiry .field{height:32px;background:var(--white);margin-bottom:9px;color:#9a9a9a;font-size:12px;font-style:italic;padding:7px 10px}
.inquiry .field.msg{height:58px;margin-bottom:14px}
.inquiry .submit{display:inline-block;background:var(--lime);color:var(--white);font-weight:700;font-size:13px;height:30px;line-height:30px;padding:0 14px}
.fcol h4{font-family:"Montserrat",Arial,sans-serif;font-size:16px;font-weight:500;display:flex;align-items:center;gap:12px;margin-bottom:18px}
.fcol h4::after{content:"";width:50px;height:1px;background:#7a848d}
.links{position:absolute;left:446px;top:51px}
.links li{list-style:none;font-size:14px;height:33px;display:flex;gap:14px}
.links li::before{content:"»"}
.details{position:absolute;left:688px;top:51px}
.details .row{display:flex;gap:12px;font-size:14px;margin-bottom:16px;align-items:flex-start;line-height:18px}
.details .row b{display:block;font-size:13.5px}
.details .row small{display:block;font-size:13px;margin-top:4px}
.flogo{position:absolute;left:990px;top:145px;text-align:center}
.flogo .brandline{display:flex;align-items:center;gap:8px;font-family:"Montserrat",Arial,sans-serif;font-weight:600;font-size:15px;letter-spacing:1px;color:#c9ced3}
.flogo .brandline .mark{width:22px;height:22px;background:#c9ced3}
.flogo .social{justify-content:center;margin-top:18px;gap:5px}
.flogo .social i{width:26px;height:26px}
.bottom{position:absolute;left:0;top:2440px;width:1200px;height:50px;background:var(--bottom);color:#c8c8c8;font-size:14px;text-align:center;line-height:50px}
</style>
</head>
<body>
<div class="page">

  <div class="topbar">
    <div class="contact">
      <span><span class="ring"><svg width="14" height="14" viewBox="0 0 24 24" fill="#fff"><path d="M6.6 10.8a15 15 0 006.6 6.6l2.2-2.2c.3-.3.7-.4 1-.2 1.1.4 2.3.6 3.6.6.6 0 1 .4 1 1V20c0 .6-.4 1-1 1A17 17 0 013 4c0-.6.4-1 1-1h3.5c.6 0 1 .4 1 1 0 1.3.2 2.5.6 3.6.1.3 0 .7-.2 1z"/></svg></span>(555)-010-2040</span>
      <span class="mail"><span class="ring"><svg width="14" height="12" viewBox="0 0 24 18" fill="#fff"><path d="M0 0h24v2L12 10 0 2z M0 4l12 8 12-8v14H0z"/></svg></span>info@meridianadvisers.com</span>
    </div>
    <div class="social"><i></i><i></i><i></i><i></i></div>
  </div>

  <header class="header">
    <div class="brand"><span class="mark"></span><span class="name">MERIDIAN ADVISERS</span></div>
    <nav class="nav">
      <a>HOME</a>
      <a>ABOUT US <span class="caret"></span></a>
      <a>SERVICES <span class="caret"></span></a>
      <a>FEATURED PROPERTIES <span class="caret"></span></a>
      <a>CONTACT US</a>
    </nav>
  </header>

  <section class="hero" role="img" aria-label="Glass office towers seen from below against a bright cloudy blue sky">
    <h1>We Are A Uniquely Collaborative Firm That Seeks To Bring A New<br>Approach To Uncovering Hidden Opportunities For Our Clients</h1>
    <div class="dots"><i></i><i></i><i></i><i></i></div>
  </section>

  <section class="welcome">
    <h2 class="title"><span><em>WELCOME TO</em> MERIDIAN ADVISERS</span></h2>
    <p class="lead">Lorem ipsum dolor sit amet, consectetuer adipiscing elit, sed diam nonummy nibh euismod tincidun.</p>
    <p class="copy">Ut wisi enim ad minim veniam, quis nostrud exerci tation ullamcorper suscipit lobortis nisl ut aliquip ex ea commodo consequat. Duis autem vel eum iriure dolor in hendrerit in vulputate velit esse molestie consequat, vel illum dolore eu feugiat nulla facilisis. am. Lorem ipsum dolor sit amet, conse ctetur piscing elit. Nulla in sollicitudin velit, bibendum velit.Cras velel facilisis ipsum, etptellnow venenatis risus.</p>
    <a class="btn">READ MORE</a>
  </section>

  <section class="featured">
    <h2 class="title"><span><em>FEATURED</em> PROPERTIES</span></h2>

    <article class="card" style="left:80px">
      <div class="photo" role="img" aria-label="Modern white two-storey house with garden" style="background:linear-gradient(180deg,#bcd3e6 0%,#e4e6e4 45%,#8a8f86 75%,#5d6b4c 100%)"><span class="tag">SALE</span></div>
      <div class="bar"><span><svg width="13" height="18" viewBox="0 0 12 17" fill="#fff"><path d="M6 0a6 6 0 016 6c0 4.5-6 11-6 11S0 10.5 0 6a6 6 0 016-6zm0 3.5a2.5 2.5 0 100 5 2.5 2.5 0 000-5z"/></svg>123 Dollar Smit Amet</span><span class="price">$ 123000</span></div>
      <h3>Duis autem vel eum iriure</h3>
      <p>Lorem ipsum dolor sit amet, consectetuer piscing elit, sed diam nonummy nibh euismod tincidunt ut laoreet dolore magna aliquam erat volutpat. Ut wisi enim ad minim veniam.</p>
      <div class="meta"><span><svg width="13" height="13" viewBox="0 0 14 14" fill="none" stroke="#888" stroke-width="1.5"><path d="M1 5V1h4M13 5V1H9M1 9v4h4M13 9v4H9"/></svg>1200 sq ft</span><span><svg width="18" height="12" viewBox="0 0 18 12" fill="#888"><path d="M0 0h2v7h16v5h-2v-2H2v2H0zM3 3h4v3H3zM8 3h9v3H8z"/></svg>2 Beds</span><span><svg width="10" height="13" viewBox="0 0 10 13" fill="#888"><path d="M5 0C5 0 0 6 0 8.5a5 5 0 0010 0C10 6 5 0 5 0z"/></svg>2 Baths</span></div>
    </article>

    <article class="card" style="left:434px">
      <div class="photo" role="img" aria-label="Contemporary white villa with lawn and shrubs" style="background:linear-gradient(180deg,#d9e4ec 0%,#eceae4 50%,#7f8a6c 80%,#4f6141 100%)"><span class="tag">RENT</span></div>
      <div class="bar"><span><svg width="13" height="18" viewBox="0 0 12 17" fill="#fff"><path d="M6 0a6 6 0 016 6c0 4.5-6 11-6 11S0 10.5 0 6a6 6 0 016-6zm0 3.5a2.5 2.5 0 100 5 2.5 2.5 0 000-5z"/></svg>123 Dollar Smit Amet</span><span class="price">$ 2120</span></div>
      <h3>Duis autem vel eum iriure</h3>
      <p>Lorem ipsum dolor sit amet, consectetuer piscing elit, sed diam nonummy nibh euismod tincidunt ut laoreet dolore magna aliquam erat volutpat. Ut wisi enim ad minim veniam.</p>
      <div class="meta"><span><svg width="13" height="13" viewBox="0 0 14 14" fill="none" stroke="#888" stroke-width="1.5"><path d="M1 5V1h4M13 5V1H9M1 9v4h4M13 9v4H9"/></svg>1200 sq ft</span><span><svg width="18" height="12" viewBox="0 0 18 12" fill="#888"><path d="M0 0h2v7h16v5h-2v-2H2v2H0zM3 3h4v3H3zM8 3h9v3H8z"/></svg>2 Beds</span><span><svg width="10" height="13" viewBox="0 0 10 13" fill="#888"><path d="M5 0C5 0 0 6 0 8.5a5 5 0 0010 0C10 6 5 0 5 0z"/></svg>2 Baths</span></div>
    </article>

    <article class="card" style="left:792px">
      <div class="photo" role="img" aria-label="Bright blue-toned office interior with glass meeting room" style="background:linear-gradient(135deg,#1d5b8c 0%,#5c98c6 40%,#cfe2ef 70%,#2e6a99 100%)"><span class="tag">SALE</span></div>
      <div class="bar"><span><svg width="13" height="18" viewBox="0 0 12 17" fill="#fff"><path d="M6 0a6 6 0 016 6c0 4.5-6 11-6 11S0 10.5 0 6a6 6 0 016-6zm0 3.5a2.5 2.5 0 100 5 2.5 2.5 0 000-5z"/></svg>123 Dollar Smit Amet</span><span class="price">$ 560000</span></div>
      <h3>Duis autem vel eum iriure</h3>
      <p>Lorem ipsum dolor sit amet, consectetuer piscing elit, sed diam nonummy nibh euismod tincidunt ut laoreet dolore magna aliquam erat volutpat. Ut wisi enim ad minim veniam.</p>
      <div class="meta"><span><svg width="13" height="13" viewBox="0 0 14 14" fill="none" stroke="#888" stroke-width="1.5"><path d="M1 5V1h4M13 5V1H9M1 9v4h4M13 9v4H9"/></svg>1200 sq ft</span><span><svg width="18" height="12" viewBox="0 0 18 12" fill="#888"><path d="M0 0h2v7h16v5h-2v-2H2v2H0zM3 3h4v3H3zM8 3h9v3H8z"/></svg>2 Beds</span><span><svg width="10" height="13" viewBox="0 0 10 13" fill="#888"><path d="M5 0C5 0 0 6 0 8.5a5 5 0 0010 0C10 6 5 0 5 0z"/></svg>2 Baths</span></div>
    </article>

    <div class="dots"><i></i><i></i><i></i><i></i></div>
  </section>

  <section class="team">
    <h2 class="title"><span><em>OUR</em> TEAM</span></h2>
    <div class="member" style="left:81px">
      <div class="photo" role="img" aria-label="Portrait of a smiling team member in an office" style="background:linear-gradient(180deg,#dfe3e6 0%,#b98a5e 60%,#8a5f3a 100%)"></div>
      <div class="name">LOREM IPSUMLOR</div>
    </div>
    <div class="member" style="left:347px">
      <div class="photo" role="img" aria-label="Portrait of a team member holding a tablet" style="background:linear-gradient(180deg,#e6ecef 0%,#9fb7d3 55%,#3e6ea8 100%)"></div>
      <div class="name">LOREM IPSUMLOR</div>
    </div>
    <div class="member active" style="left:613px">
      <div class="photo" role="img" aria-label="Portrait of a team member with a tablet, shaded by a grey overlay" style="background:linear-gradient(180deg,#a9a9a9 0%,#8f8f8f 60%,#7a7a7a 100%)"></div>
      <div class="overlay">LOREM IPSUMLOR<small>minim veniam, quis consectetur</small></div>
      <div class="name"><i></i><i></i><i></i><i></i><i></i><i></i></div>
    </div>
    <div class="member" style="left:881px">
      <div class="photo" role="img" aria-label="Portrait of a smiling team member with red hair" style="background:linear-gradient(180deg,#dde6ee 0%,#c98a63 50%,#f2f2f2 100%)"></div>
      <div class="name">LOREM IPSUMLOR</div>
    </div>
  </section>

  <footer class="footer">
    <form class="inquiry">
      <h4>QUICK INQUIRY</h4>
      <div class="field">Your Name</div>
      <div class="field">Your Email</div>
      <div class="field msg">Message</div>
      <span class="submit">SUBMIT</span>
    </form>

    <div class="fcol links">
      <h4>QUICK LINKS</h4>
      <ul><li>Home</li><li>About Us</li><li>Services</li><li>Featured Properties</li><li>Contact Us</li></ul>
    </div>

    <div class="fcol details">
      <h4>CONTACT DETAILS</h4>
      <div class="row"><svg width="13" height="18" viewBox="0 0 12 17" fill="#fff"><path d="M6 0a6 6 0 016 6c0 4.5-6 11-6 11S0 10.5 0 6a6 6 0 016-6zm0 3.5a2.5 2.5 0 100 5 2.5 2.5 0 000-5z"/></svg><div><b>MERIDIAN ADVISERS</b><small>200 Example Avenue, Sampleton 00000</small></div></div>
      <div class="row"><svg width="16" height="16" viewBox="0 0 24 24" fill="#fff"><path d="M6.6 10.8a15 15 0 006.6 6.6l2.2-2.2c.3-.3.7-.4 1-.2 1.1.4 2.3.6 3.6.6.6 0 1 .4 1 1V20c0 .6-.4 1-1 1A17 17 0 013 4c0-.6.4-1 1-1h3.5c.6 0 1 .4 1 1 0 1.3.2 2.5.6 3.6.1.3 0 .7-.2 1z"/></svg>(555)-010-2040</div>
      <div class="row"><svg width="16" height="15" viewBox="0 0 16 15" fill="#fff"><path d="M3 0h10v4H3zM0 5h16v7h-3v3H3v-3H0zM5 10v3h6v-3z"/></svg>(555)-010-2040</div>
      <div class="row"><svg width="17" height="15" viewBox="0 0 24 18" fill="none" stroke="#fff" stroke-width="2"><path d="M1 1h22v16H1zM1 1l11 9 11-9"/></svg>info@meridianadvisers.com</div>
    </div>

    <div class="flogo">
      <div class="brandline"><span class="mark"></span>MERIDIAN</div>
      <div class="social"><i></i><i></i><i></i><i></i></div>
    </div>
  </footer>

  <div class="bottom">Copyright © 2017 Meridian Advisers. All Rights Reserved.</div>
</div>
</body>
</html>
```